Petal Sprite - web design for my new Petal Studio

I would like to ask for design proposal for my newly established Petal Studio. My brand name is Petal Sprite and I focus on realisation of events and flower projects (any kind) for physical as well as legel persons. I don’t operate as a standard flowershop. I would like to have 5 key parts - 1/Landing pg/welcome, 2/About me, 3/Gallery, 4/References, 5/Contact details. I would like the web design to reflect the way I am/ I do the things, ie, be slightly different, do non-tradiotional arrangements, my passion for flowers, gentle& fregile style, love for minimalism and details in the arrangements. I attach couple of photos of what I do so that you can better understand my style . You can see more on IG mirka_petal_sprite or FB Petal Sprite. I was wondering maybe one of the first 2 photos could be part of the landing pg. Or another idea is to have a design similar to this one https://thistlebloomstudio.example, ie to choose 3-5photos which are being animated like here. However, I am open to discuss any ideas and look forward for all the proposals.

Target Market(s)

physical as well as legal persons - weddings, celebrations, business events, projects for hotels, beaty salons, restaurants and others.. actually any kind of flower project

Industry/Entity Type

flowers

Number of Pages Required

1 page

Font styles to use
Other font styles liked:
• the font which matches the logo font style

Requirements
Must have
• to reflect the way I am as described above, I prefer more simple way of design, with the attention to a detail, I prefer pastel colours

```html
<!DOCTYPE html>
<html lang="en">
<head>
<meta charset="utf-8">
<title>Petal Sprite – Petal Studio</title>
<link rel="stylesheet" href="https://fonts.googleapis.com/css2?family=Lobster+Two:wght@400;700&family=Dosis:wght@500;600;700&family=Poppins:wght@400;500;600&display=swap">
<style>
:root{
  --brown:#8a6a48;
  --brown-dark:#4b3226;
  --brown-deep:#3e281e;
  --beige:#f1e3c8;
  --paper:#f4f3f1;
  --grey-bg:#f5f5f5;
  --text:#4a4a4a;
  --ink:#2b2b2b;
  --white:#ffffff;
  --ghost:#efeeec;
}
*{box-sizing:border-box;margin:0;padding:0}
html,body{width:1200px;height:3839px;overflow:hidden}
body{position:relative;background:var(--white);font-family:"Poppins",sans-serif;color:var(--text)}
.abs{position:absolute}
.script{font-family:"Lobster Two",cursive;color:var(--brown);font-weight:400}
.display{font-family:"Dosis",sans-serif;font-weight:500;color:var(--ink)}
.divider{display:flex;gap:6px}
.divider span{display:block;width:30px;height:4px;background:var(--brown)}
.btn{position:absolute;display:flex;align-items:center;justify-content:center;font-family:"Dosis",sans-serif;font-weight:700;font-size:17px;border-radius:0 30px 0 30px;text-decoration:none}
.btn-beige{background:var(--beige);color:var(--brown-dark);box-shadow:4px 4px 0 rgba(0,0,0,.12)}
.btn-brown{background:var(--brown);color:var(--white);box-shadow:4px 4px 0 rgba(0,0,0,.15)}
.para{font-size:12.8px;line-height:28.4px;color:var(--text);text-align:justify}
.ghost{position:absolute;font-family:"Lobster Two",cursive;font-size:110px;color:var(--ghost);white-space:nowrap;line-height:1}

.site-header{left:0;top:0;width:1200px;height:105px;background:var(--paper)}
.nav a{position:absolute;top:44px;font-family:"Dosis",sans-serif;font-weight:600;font-size:15px;color:var(--ink);text-decoration:none}
.nav a.active{color:var(--brown)}
.brand{left:530px;top:18px;width:120px;text-align:center;font-family:"Dosis",sans-serif;font-weight:600;font-size:18px;color:var(--brown);display:flex;flex-direction:column;align-items:center;gap:6px}
.brand i{display:block;width:30px;height:30px;border:2px solid var(--brown);border-radius:50%}
.book{left:720px;top:30px;width:214px;height:60px;border:2px solid var(--ink);color:var(--ink);font-size:16px;background:transparent}
.login{left:942px;top:30px;width:146px;height:60px;background:var(--beige);color:var(--brown-dark);font-size:16px;gap:8px}

.hero{left:0;top:105px;width:1200px;height:598px;background:linear-gradient(100deg,#6b4f2c 0%,#c9a030 22%,#d7b24a 40%,#b8bcc4 65%,#9aa3b1 100%)}
.hero-panel{left:595px;top:249px;width:605px;height:309px;background:rgba(120,98,74,.78)}
.hero-title{left:629px;top:262px;font-size:66px;color:var(--white)}
.hero-text{left:629px;top:352px;width:520px;font-size:15px;line-height:33px;color:var(--white)}
.dots{left:568px;top:653px;display:flex;gap:4px}
.dots span{width:13px;height:13px;border:2px solid var(--white);border-radius:50%}
.dots span.on{background:var(--white)}

.portrait{left:630px;top:770px;width:470px;height:510px}

.gallery-photo{left:0;top:1360px;width:600px;height:685px;background:linear-gradient(160deg,#4b3a2a 0%,#5e6d3a 35%,#8a9a68 55%,#4f3a2a 100%)}
.gallery-side{left:600px;top:1360px;width:600px;height:685px;background:var(--grey-bg);overflow:hidden}
.view-more{left:642px;top:1752px;font-family:"Dosis",sans-serif;font-weight:600;font-size:18px;color:var(--brown);display:flex;align-items:center;gap:8px}
.thumb{top:1853px;width:315px;height:282px;border:4px solid var(--white);box-shadow:0 2px 8px rgba(0,0,0,.2)}

.references{left:0;top:2045px;width:1200px;height:635px;background:radial-gradient(ellipse at 50% 55%,#5a3d2d 0%,var(--brown-deep) 70%)}
.center{left:0;width:1200px;text-align:center}

.field{position:absolute;font-size:15px;color:#777}
.field-line{position:absolute;height:2px;background:#777}
.submit{left:471px;top:3245px;width:259px;height:51px;background:#47291e;color:var(--white);border-radius:26px;font-family:"Poppins",sans-serif;font-weight:600;font-size:16px}
.info-icon{position:absolute;width:54px;height:54px;border-radius:50%;background:var(--brown);display:flex;align-items:center;justify-content:center}
.info-title{position:absolute;font-family:"Dosis",sans-serif;font-weight:500;font-size:18px;color:var(--ink)}
.info-text{position:absolute;font-size:15px;line-height:26px;color:var(--text)}

.site-footer{left:0;top:3493px;width:1200px;height:292px;background:var(--brown)}
.footer-bar{left:0;top:3785px;width:1200px;height:54px;background:#7a5b3b}
.footer-head{color:var(--white)}
.footer-links{list-style:none;font-size:13px;color:var(--white)}
.footer-links li{height:29.5px;display:flex;align-items:center;gap:8px}
.social{top:3660px;width:33px;height:33px;background:#2b1d14}
</style>
</head>
<body>

<header class="abs site-header">
  <nav class="nav">
    <a class="active" style="left:110px">Home</a>
    <a style="left:176px">About Me</a>
    <a style="left:264px">Gallery</a>
    <a style="left:339px">Reference</a>
    <a style="left:437px">Contact</a>
  </nav>
  <div class="abs brand"><i></i>Petal Sprite</div>
  <a class="btn book">Book a Appointment</a>
  <a class="btn login">
    <svg width="13" height="15" viewBox="0 0 13 15"><circle cx="6.5" cy="4" r="3.6" fill="#4b3226"/><path d="M0 15c0-4 3-6 6.5-6S13 11 13 15z" fill="#4b3226"/></svg>Login</a>
</header>

<section class="abs hero" role="img" aria-label="Vase of red, white and yellow ranunculus on a round side table beside a mustard armchair"></section>
<div class="abs hero-panel"></div>
<h1 class="abs script hero-title">Petal Studio</h1>
<p class="abs hero-text">Lorem ipsum dolor sit amet, consectetur adipiscing elit, sed do eiusmod tempor incididunt ut labore et dolore magna aliqua. Ut enim ad minim veniam, quis</p>
<a class="btn btn-beige" style="left:629px;top:470px;width:214px;height:60px">Get Started</a>
<div class="abs dots"><span></span><span></span><span class="on"></span><span></span></div>

<section class="about">
  <div class="ghost" style="left:-22px;top:1100px;transform:rotate(-90deg);transform-origin:left top">About me</div>
  <h2 class="abs script" style="left:112px;top:782px;font-size:44px">About me</h2>
  <p class="abs display" style="left:112px;top:843px;width:460px;font-size:26px;line-height:37px">Lorem ipsum dolor sit amet, consectetur adipiscing elit, sed do eiusmod tempor</p>
  <div class="abs divider" style="left:112px;top:931px"><span></span><span></span><span></span></div>
  <p class="abs para" style="left:112px;top:960px;width:448px">Lorem ipsum dolor sit amet, consectetur adipiscing elit, sed do eiusmod tempor incididunt ut labore et dolore magna aliqua. Ut enim ad minim veniam, quis nostrud exercitation ullamco laboris nisi ut aliquip ex ea commodo consequat. Duis aute irure dolor in reprehenderit in voluptate velit esse cillum dolore eu fugiat nulla pariatur. Excepteur sint occaecat cupidatat non proident, sunt in culpa qui officia deserunt mollit anim id est laborum</p>
  <a class="btn btn-brown" style="left:112px;top:1183px;width:213px;height:60px">Read More</a>
  <svg class="abs portrait" viewBox="0 0 470 510" role="img" aria-label="Portrait of the florist in a mustard sweater against a soft autumn background">
    <defs><linearGradient id="pg" x1="0" y1="0" x2="0" y2="1"><stop offset="0" stop-color="#ecdcb6"/><stop offset=".55" stop-color="#d9a96a"/><stop offset="1" stop-color="#cf9a2e"/></linearGradient></defs>
    <path d="M14 300 A222 222 0 0 1 456 300" fill="none" stroke="#8a6a48" stroke-width="16"/>
    <circle cx="235" cy="280" r="222" fill="url(#pg)"/>
  </svg>
</section>

<div class="abs gallery-photo" role="img" aria-label="Large wild bouquet of greenery, white and lilac blooms against a wooden wall"></div>
<div class="abs gallery-side"></div>
<div class="ghost" style="left:1090px;top:2010px;transform:rotate(-90deg);transform-origin:left top">Our Gallery</div>
<h2 class="abs script" style="left:642px;top:1445px;font-size:42px">Our Gallery</h2>
<p class="abs display" style="left:642px;top:1505px;width:460px;font-size:26px;line-height:37px">Lorem ipsum dolor sit amet, consectetur adipiscing elit, sed do eiusmod tempor</p>
<div class="abs divider" style="left:642px;top:1594px"><span></span><span></span><span></span></div>
<p class="abs para" style="left:642px;top:1622px;width:446px">Lorem ipsum dolor sit amet, consectetur adipiscing elit, sed do eiusmod tempor incididunt ut labore et dolore magna aliqua. Ut enim ad minim veniam, quis nostrud exercitation ullamco laboris nisi ut aliquip ex ea commodo consequat.</p>
<div class="abs view-more">View More Our Gallery
  <svg width="18" height="18" viewBox="0 0 18 18"><circle cx="9" cy="9" r="9" fill="#8a6a48"/><path d="M7 5l4 4-4 4" stroke="#fff" stroke-width="2" fill="none"/></svg></div>
<svg class="abs" style="left:1050px;top:1808px" width="40" height="20" viewBox="0 0 40 20"><path d="M10 3l-6 7 6 7M30 3l6 7-6 7" stroke="#2b2b2b" stroke-width="2" fill="none"/></svg>
<div class="abs thumb" style="left:113px;background:linear-gradient(160deg,#7a4a3a,#c98a7a 45%,#6a6a4a)" role="img" aria-label="Protea arrangement in a stone vase against a brick wall"></div>
<div class="abs thumb" style="left:444px;background:radial-gradient(circle at 50% 55%,#d7dce0,#7a8a5a 50%,#2e3a2a)" role="img" aria-label="Daisies and moss in a glass bowl"></div>
<div class="abs thumb" style="left:773px;background:linear-gradient(120deg,#6a6a3a,#d9c24a 45%,#e7b59a 70%,#efe6d8)" role="img" aria-label="Yellow and peach bouquet held in front of a woman"></div>

<section class="abs references" role="img" aria-label="Dimmed photo of a flower bowl on a table"></section>
<h2 class="abs center script" style="top:2210px;font-size:42px;color:var(--beige)">References</h2>
<p class="abs center display" style="top:2270px;font-size:26px;line-height:37px;color:var(--white)">Lorem ipsum dolor sit amet, consectetur adipiscing<br>elit, sed do eiusmod tempor</p>
<div class="abs divider" style="left:548px;top:2358px"><span style="background:var(--beige)"></span><span style="background:var(--beige)"></span><span style="background:var(--beige)"></span></div>
<p class="abs center" style="top:2390px;color:var(--white);padding:0 160px;font-size:13px;line-height:28.4px">Lorem ipsum dolor sit amet, consectetur adipiscing elit, sed do eiusmod tempor incididunt ut labore et dolore magna aliqua. Ut enim ad minim veniam, quis nostrud exercitation ullamco laboris nisi ut aliquip ex ea commodo consequat. Duis aute irure dolor in reprehenderit in voluptate velit esse cillum dolore eu fugiat nulla pariatur. Excepteur sint occaecat cupidatat non proident, sunt in culpa qui officia deserunt mollit anim id est laborum</p>
<a class="btn btn-beige" style="left:493px;top:2520px;width:214px;height:60px">Get Started</a>

<div class="abs" style="left:360px;top:2800px;width:480px;height:690px;background:radial-gradient(ellipse at 50% 45%,#f3f1ea 0%,#ffffff 70%)" role="img" aria-label="Faint vase of white flowers behind the form"></div>
<div class="ghost" style="left:5px;top:3115px;transform:rotate(-90deg);transform-origin:left top">Contact Us</div>
<h2 class="abs center script" style="top:2740px;font-size:42px">Contact Us</h2>
<p class="abs center display" style="top:2805px;font-size:26px;line-height:37px">Lorem ipsum dolor sit amet, consectetur adipiscing<br>elit, sed do eiusmod tempor</p>
<div class="abs divider" style="left:548px;top:2894px"><span></span><span></span><span></span></div>
<span class="field" style="left:228px;top:2955px">First Name</span>
<span class="field-line" style="left:228px;top:2984px;width:349px"></span>
<span class="field" style="left:623px;top:2955px">Last Name</span>
<span class="field-line" style="left:623px;top:2984px;width:350px"></span>
<span class="field" style="left:228px;top:3025px">Email Address</span>
<span class="field-line" style="left:228px;top:3054px;width:349px"></span>
<span class="field" style="left:623px;top:3025px">Phone Number</span>
<span class="field-line" style="left:623px;top:3054px;width:350px"></span>
<span class="field" style="left:228px;top:3087px">Message</span>
<span class="field-line" style="left:228px;top:3192px;width:740px"></span>
<a class="btn submit">Submit Now</a>

<div class="info-icon" style="left:140px;top:3348px"><svg width="18" height="24" viewBox="0 0 18 24"><path d="M9 0a9 9 0 0 0-9 9c0 7 9 15 9 15s9-8 9-15a9 9 0 0 0-9-9z" fill="#fff"/><circle cx="9" cy="9" r="3.3" fill="#8a6a48"/></svg></div>
<span class="info-title" style="left:213px;top:3350px">ADDRESS</span>
<span class="info-text" style="left:213px;top:3377px;width:270px">1234, Lorem ipsum dolor sit amet, consectetur adipiscing</span>
<div class="info-icon" style="left:518px;top:3348px"><svg width="22" height="22" viewBox="0 0 24 24"><path d="M6.6 10.8a15 15 0 0 0 6.6 6.6l2.2-2.2c.3-.3.7-.4 1-.2 1.1.4 2.3.6 3.6.6.6 0 1 .4 1 1V20c0 .6-.4 1-1 1A17 17 0 0 1 3 4c0-.6.4-1 1-1h3.5c.6 0 1 .4 1 1 0 1.3.2 2.5.6 3.6.1.3 0 .7-.2 1z" fill="#fff"/></svg></div>
<span class="info-title" style="left:592px;top:3350px">CALL NOW</span>
<span class="info-text" style="left:592px;top:3377px">+1 888-888-8888</span>
<div class="info-icon" style="left:816px;top:3348px"><svg width="24" height="18" viewBox="0 0 24 18"><rect width="24" height="18" rx="2" fill="#fff"/><path d="M1 1l11 9 11-9" stroke="#8a6a48" stroke-width="2" fill="none"/></svg></div>
<span class="info-title" style="left:890px;top:3350px">EMAIL</span>
<span class="info-text" style="left:890px;top:3377px">hello@petalstudio.example</span>

<footer class="abs site-footer"></footer>
<h3 class="abs script footer-head" style="left:108px;top:3540px;font-size:48px">About Us</h3>
<p class="abs" style="left:108px;top:3620px;width:366px;font-size:12px;line-height:26px;color:var(--white);text-align:justify">Lorem ipsum dolor sit amet, consectetur adipiscing elit, sed do eiusmod tempor incididunt ut labore et dolore magna aliqua. Ut enim ad minim veniam, quis nostrud exercitation ullamco laboris nisi ut aliquip ex ea commodo consequat. Duis aute irure dolor in reprehenderit</p>
<h3 class="abs script footer-head" style="left:537px;top:3550px;font-size:22px">Quick Links</h3>
<ul class="abs footer-links" style="left:537px;top:3595px">
  <li>» Home</li><li>» About Me</li><li>» Gallery</li><li>» Reference</li><li>» Contact Us</li>
</ul>
<ul class="abs footer-links" style="left:722px;top:3595px">
  <li>» Reviews</li><li>» FAQ's</li><li>» Help</li>
</ul>
<h3 class="abs script footer-head" style="left:895px;top:3550px;font-size:22px">Contact Us</h3>
<svg class="abs" style="left:897px;top:3594px" width="34" height="34" viewBox="0 0 34 34"><circle cx="17" cy="17" r="15.5" fill="none" stroke="#fff" stroke-width="1.5"/><path d="M12.5 15.5a9 9 0 0 0 6 6l1.6-1.6c.2-.2.5-.3.8-.1l2.6.5v2.7c0 .4-.3.7-.7.7A11.5 11.5 0 0 1 9.5 10.7c0-.4.3-.7.7-.7h2.7l.5 2.6c.1.3 0 .6-.2.8z" fill="#fff"/></svg>
<span class="abs" style="left:937px;top:3601px;font-size:15px;font-weight:600;color:var(--white)">+1 888 888 8888</span>
<span class="abs social" style="left:907px"></span>
<span class="abs social" style="left:953px"></span>
<span class="abs social" style="left:1000px"></span>
<span class="abs social" style="left:1045px"></span>
<div class="abs footer-bar"></div>
<p class="abs center" style="top:3802px;font-size:14px;font-weight:500;color:var(--white)">© 2022 All Rights Reserved</p>

</body>
</html>
```